Corporate Identity for our Company

For this project we need to explain a few things:
We started off in 1933 as a food processing company with main business of Edible oil sold as T Seal. The main colour were red, black and white but those were simple times. The design became immensely popular because of good product and great marketing. Later on We used a lot of yellow as well on the background for our product designs, wall painting etc and also the label. So the colours of our company became RED, YELLOW, BLACK & WHITE. Please check the website for reference http://zenwaygrainworks.com/edible-oils.php
The family business divided into two parts in 1995. We got T seal for items agonised in class 30 of Indian trademark act & our cousins for class 29. We have since only focused on wheat products and are now looking at capitalising our benefits for other products in class 30 which are food items like Besan, Lentils, salt, spices etc. ( for a complete list please visit http://www.quiblex.com/legal-encyclopedia/trademark-class-30-coffee-flour-rice-products.html)
We have also made a website please check : http://vantelhubdock.net/~tseal/
Username : rovelpage
Password : wendrix@Glade72
You can help by redesigning our stationery, letter pads etc. so we can maintain consistency that enables customer recall/ recognition for our company's profile.
I'm attaching pictures of our current stationary (letter pads) and pictures of our products. This will help you get an idea about our company's current design patterns.
Letter pad:
Dimensions/Size: A4
colours: Any
Information to be added:
Admin. office: 7 B/D Stock Shed,
Jammu (J&K)
Ph. no.: 0191-2867403 ; Fax: 0191-2867459
Units:
Sona Kiran Flour Mills
New Sona Kiran Flour Mills
Lane No. 9
TEMBRA Industrial Complex,
Kesar Vihar, Rampur (J&K)
Ph no. 0192-3584076
Email: support@tsealgoods.com
1) Business cards:
Dimensions: L x B (3.5" x 2 ") printable size
Colours: multi colour
Information:
should contain the T seal logo,
Name of the person
company Address (which you have already)
ph no (we will fill that in)
and email. (we will fill that in)
2) Envelopes:
Dimensions:
L x B (14" x 12")
Colour: Multi
information: T seal logo
contact information and address

```html
<!DOCTYPE html>
<html lang="en">
<head>
<meta charset="utf-8">
<title>T Seal Business Card</title>
<link href="https://fonts.googleapis.com/css2?family=Gelasio:wght@400;700&display=swap" rel="stylesheet">
<style>
  :root {
    --stage: #ece8e2;
    --yellow-light: #fff27a;
    --yellow: #ffe01a;
    --yellow-deep: #fdd000;
    --red: #d4231f;
    --rule: #e58a84;
    --ink: #1c1c1c;
    --paper: #ffffff;
    --edge: #2a2a2a;
  }
  * { box-sizing: border-box; margin: 0; padding: 0; }
  html, body { width: 1200px; height: 1000px; overflow: hidden; }
  body {
    background: var(--stage);
    font-family: "Gelasio", Georgia, serif;
    color: var(--ink);
    position: relative;
  }
  .card {
    position: absolute;
    top: 200px;
    width: 358px;
    height: 629px;
    border-radius: 14px;
    overflow: hidden;
    box-shadow: 0 4px 14px rgba(0,0,0,0.25);
  }
  .card-front {
    left: 243px;
    background: radial-gradient(ellipse at 50% 45%, var(--yellow-light) 0%, var(--yellow) 55%, var(--yellow-deep) 100%);
  }
  .card-back {
    left: 627px;
    background: var(--paper);
    border: 1px solid var(--edge);
  }
  .brand {
    position: absolute;
    left: 0; right: 0;
    text-align: center;
    color: var(--ink);
    font-weight: 700;
  }
  .card-front .brand { top: 282px; font-size: 44px; }
  .card-back .brand { top: 112px; font-size: 30px; }
  .website {
    position: absolute;
    left: 0; right: 0;
    bottom: 28px;
    text-align: center;
    color: var(--red);
    font-size: 19px;
  }
  .person {
    position: absolute;
    top: 290px;
    left: 0; right: 0;
    text-align: center;
  }
  .person-name { font-size: 19px; font-weight: 700; line-height: 26px; }
  .person-title { font-size: 15px; line-height: 20px; }
  .divider {
    position: absolute;
    top: 399px;
    left: 30px;
    width: 299px;
    height: 2px;
    background: var(--rule);
  }
  .contact {
    position: absolute;
    left: 0; right: 0;
    text-align: center;
    font-size: 15px;
    line-height: 19px;
  }
  .contact-admin { top: 415px; }
  .contact-units { top: 490px; }
  .contact-label { text-decoration: underline; }
</style>
</head>
<body>
  <section class="card card-front">
    <div class="brand">T Seal</div>
    <p class="website">www.tsealgoods.com</p>
  </section>

  <section class="card card-back">
    <div class="brand">T Seal</div>
    <div class="person">
      <p class="person-name">Arvind Kohli</p>
      <p class="person-title">Managing Director</p>
    </div>
    <div class="divider"></div>
    <div class="contact contact-admin">
      <p><span class="contact-label">Admin. Office</span>:</p>
      <p>7 B/D Stock Shed, Jammu (J&amp;K)</p>
      <p>P: 0191-2867403,&nbsp; F: 0191-2867459</p>
    </div>
    <div class="contact contact-units">
      <p><span class="contact-label">Units</span>:</p>
      <p>Sona Kiran Flour Mills,</p>
      <p>TEMBRA Industrial Complex, Lane No. 9</p>
      <p>Kesar Vihar, Rampur (J&amp;K)</p>
      <p>P: 0192-3584076</p>
      <p>E: support@tsealgoods.com</p>
    </div>
  </section>
</body>
</html>
```